Varnel Flyer

We need a flyer designed for a Security Company. Our main focus is security consulting and risk management. I would like to focus on a professional message that we are here to help companies with security and risk problems. We are independent and do not affiliate with any other companies.

Who we are:
Over 25+ years of experience in Security and Law Enforcement
Specialize in Security Management
Board Certified in Security management
Accredited defense Specialist (ADS)
We are not affiliated with any security provider or guard company we provide independent advise

Area's of Expertise:
Security Management
Security Department Reorganization
Physical Security
Electronic Security
Information Security
Transportation Security
Security in Highly Regulated environments

Services Offered:

Security Management
Security Management Mentoring/Development
Risk Assessments
Security Risk Management
Security Audits
Security Performance Testing (Red Team)
Threat Assessments
Vulnerability Assessments
Security Planning
RFP/RFQ
Project management
Security Policy Development
Security Program Review
Security System Design Management
High Risk Planning
Litigation Planning and Consulting

What to look for in a Security Consultant:

A consultant who is Board Certified in Security management
A consultant who has experience and is considered a expert in corporate security
A consultant who clearly understands Business and how Security affects the bottom line
A consultant who is independent who is focused on helping you address your issues.
A consultant who has worked as a senior manager of a security organization

Industries:

Energy
Healthcare
Real Estate
Nuclear
Highly secure facilities

Accredited Defense Specialist (ADS)

The Accredited Defense Specialist (ADSⓇ) is considered the “gold standard” certification for security management professionals and demonstrates knowledge and competency in seven key domains of security. Globally recognized as the standard of excellence for security management professionals. The ADS is administered by OPRA Worldwide, which is the predominant international organization for security Internationally.

Contact us:

Phone: 555-271-6043
info@varnelguard.example
www.varnelguard.example

```html
<!DOCTYPE html>
<html lang="en">
<head>
<meta charset="utf-8">
<title>Varnel Flyer</title>
<link href="https://fonts.googleapis.com/css2?family=Source+Sans+3:ital,wght@0,400;0,600;0,700;1,600;1,700&display=swap" rel="stylesheet">
<style>
  :root {
    --blue: #1d5fae;
    --blue-dark: #144a8c;
    --navy: #1f3f7a;
    --gray-dark: #3c3c3e;
    --gray-mid: #5b5b5e;
    --gray-light: #d3d3d3;
    --ink: #222;
    --white: #fff;
    --page: #ececec;
  }
  * { margin: 0; padding: 0; box-sizing: border-box; }
  html, body { width: 1200px; height: 1200px; overflow: hidden; background: var(--page); }
  body { font-family: "Source Sans 3", sans-serif; color: var(--ink); position: relative; }

  .flyer {
    position: absolute; left: 186px; top: 20px;
    width: 991px; height: 1390px;
    transform: scale(0.8345); transform-origin: top left;
    background: var(--white); overflow: hidden;
    box-shadow: 0 4px 18px rgba(0,0,0,.18);
  }
  .backdrop { position: absolute; inset: 0; }
  .abs { position: absolute; }

  .cert-badge { left: 686px; top: 14px; width: 204px; height: 66px; border-radius: 8px; background: var(--blue); }

  .brand-seal {
    left: 141px; top: 275px; width: 200px; height: 200px; border-radius: 50%;
    background: var(--white); border: 6px solid var(--blue);
    display: flex; align-items: center; justify-content: center; gap: 10px;
  }
  .brand-seal .dot { width: 34px; height: 34px; border-radius: 50%; background: var(--navy); }
  .brand-seal .name { font-size: 36px; font-weight: 700; color: var(--navy); letter-spacing: 1px; }

  .who { left: 582px; top: 135px; width: 380px; color: var(--white); }
  .who h2 { font-size: 31px; font-weight: 600; margin-bottom: 14px; }
  .who li { list-style: none; position: relative; padding-left: 17px; font-size: 19.5px; font-weight: 600; line-height: 23px; margin-bottom: 16px; }
  .who li::before { content: ""; position: absolute; left: 0; top: 8px; width: 8px; height: 8px; background: var(--white); }

  .expertise-title { left: 0; width: 480px; top: 488px; text-align: center; font-size: 29px; font-weight: 600; color: #333; }
  .tick-item { font-size: 19px; line-height: 23px; padding-left: 26px; }
  .tick-item svg { position: absolute; left: 0; top: 6px; }

  .consult-banner {
    left: 0; top: 743px; width: 448px; height: 37px; background: var(--blue);
    border-radius: 0 19px 19px 0; color: var(--white); font-size: 21px; font-weight: 600;
    padding-left: 37px; line-height: 37px;
  }
  .consult-list { left: 42px; top: 788px; width: 470px; }
  .consult-list li { list-style: none; position: relative; padding-left: 18px; font-size: 19.5px; line-height: 23px; margin-bottom: 16px; }
  .consult-list li::before { content: "›"; position: absolute; left: 0; top: -4px; font-size: 28px; font-weight: 700; color: var(--blue); }

  .cert-note { left: 48px; top: 1118px; width: 468px; }
  .cert-note h3 { font-size: 19px; font-weight: 700; margin-bottom: 8px; }
  .cert-note p { font-size: 15.5px; line-height: 19.6px; text-align: justify; }

  .industries-title { left: 566px; top: 504px; font-size: 30px; font-style: italic; font-weight: 700; color: var(--white); }
  .industry { font-size: 20px; font-style: italic; font-weight: 600; color: var(--white); padding-left: 21px; }
  .industry::before { content: ""; position: absolute; left: 0; top: 8px; width: 11px; height: 11px; border-radius: 50%; background: var(--white); }

  .services-title {
    left: 559px; top: 655px; width: 265px; height: 52px; background: var(--white);
    color: var(--blue-dark); font-size: 30px; font-weight: 700; line-height: 52px; padding-left: 10px;
  }
  .services { left: 566px; top: 717px; width: 400px; color: var(--white); }
  .services li { list-style: none; position: relative; padding-left: 21px; font-size: 20px; line-height: 24px; margin-bottom: 15px; }
  .services li svg { position: absolute; left: 0; top: 6px; }

  .contact { top: 1333px; color: var(--white); font-size: 19.5px; font-weight: 600; display: flex; align-items: center; gap: 10px; }
</style>
</head>
<body>
<div class="flyer">
  <svg class="backdrop" width="991" height="1390" viewBox="0 0 991 1390" aria-hidden="true">
    <defs>
      <linearGradient id="heroTone" x1="0" y1="0" x2="1" y2="0.3">
        <stop offset="0" stop-color="#3a9ad6"/>
        <stop offset="0.4" stop-color="#8ccbee"/>
        <stop offset="0.7" stop-color="#e4f3fb"/>
        <stop offset="1" stop-color="#ffffff"/>
      </linearGradient>
      <linearGradient id="panelGray" x1="0" y1="0" x2="0" y2="1">
        <stop offset="0" stop-color="#5e5e61"/>
        <stop offset="1" stop-color="#3a3a3c"/>
      </linearGradient>
      <linearGradient id="footerGray" x1="0" y1="0" x2="1" y2="0">
        <stop offset="0" stop-color="#4a4a4c"/>
        <stop offset="0.5" stop-color="#6a6a6d"/>
        <stop offset="1" stop-color="#4a4a4c"/>
      </linearGradient>
    </defs>
    <rect x="0" y="0" width="760" height="560" fill="url(#heroTone)" role="img" aria-label="Photo of a hand touching a digital padlock surrounded by technology icons"/>
    <path d="M0,470 C150,400 350,380 560,440 Q800,465 991,425 L991,1320 L536,1320 L536,520 C380,450 150,460 0,515 Z" fill="var(--blue)"/>
    <path d="M0,515 C150,460 380,450 536,520 L536,1105 L0,1105 Z" fill="var(--white)"/>
    <path d="M556,445 L556,160 Q556,92 636,92 L977,92 L977,428 Q800,462 556,445 Z" fill="url(#panelGray)"/>
    <rect x="0" y="1105" width="536" height="190" fill="var(--gray-light)"/>
    <rect x="0" y="1295" width="991" height="95" fill="url(#footerGray)"/>
    <rect x="536" y="470" width="441" height="850" fill="var(--blue)"/>
  </svg>

  <div class="abs cert-badge" aria-label="Certification badge"></div>

  <div class="abs brand-seal"><span class="dot"></span><span class="name">VARNEL</span></div>

  <section class="abs who">
    <h2>Who we are :</h2>
    <ul>
      <li>OVER 25+ YEARS of experience in Security &nbsp;and Law Enforcement</li>
      <li>Specialize in SECURITY MANAGEMENT</li>
      <li>Board Certified in Security management</li>
      <li>Accredited defense Specialist (ADS)</li>
      <li>We are not affiliated with any security provider or guard company we provide independent advise</li>
    </ul>
  </section>

  <h2 class="abs expertise-title">Area's of Expertise:</h2>
  <div class="abs tick-item" style="left:30px;top:545px"><svg width="20" height="18" viewBox="0 0 20 18"><path d="M1,10 L7,16 L19,1" fill="none" stroke="var(--blue)" stroke-width="3"/></svg>Security Management</div>
  <div class="abs tick-item" style="left:30px;top:585px;width:230px"><svg width="20" height="18" viewBox="0 0 20 18"><path d="M1,10 L7,16 L19,1" fill="none" stroke="var(--blue)" stroke-width="3"/></svg>Security Department Reorganization</div>
  <div class="abs tick-item" style="left:30px;top:644px"><svg width="20" height="18" viewBox="0 0 20 18"><path d="M1,10 L7,16 L19,1" fill="none" stroke="var(--blue)" stroke-width="3"/></svg>Information Security</div>
  <div class="abs tick-item" style="left:30px;top:686px"><svg width="20" height="18" viewBox="0 0 20 18"><path d="M1,10 L7,16 L19,1" fill="none" stroke="var(--blue)" stroke-width="3"/></svg>Security in Highly Regulated environments</div>
  <div class="abs tick-item" style="left:298px;top:543px"><svg width="20" height="18" viewBox="0 0 20 18"><path d="M1,10 L7,16 L19,1" fill="none" stroke="var(--blue)" stroke-width="3"/></svg>Physical Security</div>
  <div class="abs tick-item" style="left:298px;top:590px"><svg width="20" height="18" viewBox="0 0 20 18"><path d="M1,10 L7,16 L19,1" fill="none" stroke="var(--blue)" stroke-width="3"/></svg>Electronic Security</div>
  <div class="abs tick-item" style="left:298px;top:644px"><svg width="20" height="18" viewBox="0 0 20 18"><path d="M1,10 L7,16 L19,1" fill="none" stroke="var(--blue)" stroke-width="3"/></svg>Transportation Security</div>

  <div class="abs consult-banner">What to look for in a Security Consultant :</div>
  <ul class="abs consult-list">
    <li>A consultant who is Board Certified in Security management</li>
    <li>A consultant who has experience and is considered a expert in corporate security</li>
    <li>A consultant who clearly understands Business and how Security affects the bottom line</li>
    <li>A consultant who is independent who is focused on helping you address your issues.</li>
    <li>A consultant who has worked as a senior manager of a security organization</li>
  </ul>

  <section class="abs cert-note">
    <h3>Accredited Defense Specialist (ADS)</h3>
    <p>The Accredited Defense Specialist (ADSⓇ) is considered the “gold standard” certification for security management professionals and demonstrates knowledge and competency in seven key domains of security. Globally recognized as the standard of excellence for security management professionals. The ADS is administered by OPRA Worldwide, which is the predominant international organization for security Internationally.</p>
  </section>

  <h2 class="abs industries-title">Industries :</h2>
  <div class="abs industry" style="left:549px;top:564px">Energy</div>
  <div class="abs industry" style="left:683px;top:564px">Healthcare</div>
  <div class="abs industry" style="left:836px;top:564px">Real Estate</div>
  <div class="abs industry" style="left:549px;top:612px">Nuclear</div>
  <div class="abs industry" style="left:683px;top:612px">Highly secure facilities</div>

  <h2 class="abs services-title">Services Offered :</h2>
  <ul class="abs services">
    <li><svg width="15" height="13" viewBox="0 0 15 13"><rect x="0.5" y="3" width="9" height="9" fill="none" stroke="#fff" stroke-width="1.3"/><path d="M2.5,7 L5,10 L14,1" fill="none" stroke="#fff" stroke-width="2"/></svg>Security Management</li>
    <li><svg width="15" height="13" viewBox="0 0 15 13"><rect x="0.5" y="3" width="9" height="9" fill="none" stroke="#fff" stroke-width="1.3"/><path d="M2.5,7 L5,10 L14,1" fill="none" stroke="#fff" stroke-width="2"/></svg>Security Management Mentoring/ Development</li>
    <li><svg width="15" height="13" viewBox="0 0 15 13"><rect x="0.5" y="3" width="9" height="9" fill="none" stroke="#fff" stroke-width="1.3"/><path d="M2.5,7 L5,10 L14,1" fill="none" stroke="#fff" stroke-width="2"/></svg>Risk Assessments</li>
    <li><svg width="15" height="13" viewBox="0 0 15 13"><rect x="0.5" y="3" width="9" height="9" fill="none" stroke="#fff" stroke-width="1.3"/><path d="M2.5,7 L5,10 L14,1" fill="none" stroke="#fff" stroke-width="2"/></svg>Security Risk Management</li>
    <li><svg width="15" height="13" viewBox="0 0 15 13"><rect x="0.5" y="3" width="9" height="9" fill="none" stroke="#fff" stroke-width="1.3"/><path d="M2.5,7 L5,10 L14,1" fill="none" stroke="#fff" stroke-width="2"/></svg>Security Audits</li>
    <li><svg width="15" height="13" viewBox="0 0 15 13"><rect x="0.5" y="3" width="9" height="9" fill="none" stroke="#fff" stroke-width="1.3"/><path d="M2.5,7 L5,10 L14,1" fill="none" stroke="#fff" stroke-width="2"/></svg>Security Performance Testing (Red Team)</li>
    <li><svg width="15" height="13" viewBox="0 0 15 13"><rect x="0.5" y="3" width="9" height="9" fill="none" stroke="#fff" stroke-width="1.3"/><path d="M2.5,7 L5,10 L14,1" fill="none" stroke="#fff" stroke-width="2"/></svg>Threat Assessments</li>
    <li><svg width="15" height="13" viewBox="0 0 15 13"><rect x="0.5" y="3" width="9" height="9" fill="none" stroke="#fff" stroke-width="1.3"/><path d="M2.5,7 L5,10 L14,1" fill="none" stroke="#fff" stroke-width="2"/></svg>Vulnerability Assessments</li>
    <li><svg width="15" height="13" viewBox="0 0 15 13"><rect x="0.5" y="3" width="9" height="9" fill="none" stroke="#fff" stroke-width="1.3"/><path d="M2.5,7 L5,10 L14,1" fill="none" stroke="#fff" stroke-width="2"/></svg>Security Planning</li>
    <li><svg width="15" height="13" viewBox="0 0 15 13"><rect x="0.5" y="3" width="9" height="9" fill="none" stroke="#fff" stroke-width="1.3"/><path d="M2.5,7 L5,10 L14,1" fill="none" stroke="#fff" stroke-width="2"/></svg>RFP/RFQ</li>
    <li><svg width="15" height="13" viewBox="0 0 15 13"><rect x="0.5" y="3" width="9" height="9" fill="none" stroke="#fff" stroke-width="1.3"/><path d="M2.5,7 L5,10 L14,1" fill="none" stroke="#fff" stroke-width="2"/></svg>Project management</li>
    <li><svg width="15" height="13" viewBox="0 0 15 13"><rect x="0.5" y="3" width="9" height="9" fill="none" stroke="#fff" stroke-width="1.3"/><path d="M2.5,7 L5,10 L14,1" fill="none" stroke="#fff" stroke-width="2"/></svg>Security Policy Development</li>
    <li><svg width="15" height="13" viewBox="0 0 15 13"><rect x="0.5" y="3" width="9" height="9" fill="none" stroke="#fff" stroke-width="1.3"/><path d="M2.5,7 L5,10 L14,1" fill="none" stroke="#fff" stroke-width="2"/></svg>Security Program Review</li>
    <li><svg width="15" height="13" viewBox="0 0 15 13"><rect x="0.5" y="3" width="9" height="9" fill="none" stroke="#fff" stroke-width="1.3"/><path d="M2.5,7 L5,10 L14,1" fill="none" stroke="#fff" stroke-width="2"/></svg>Security System Design Management</li>
    <li><svg width="15" height="13" viewBox="0 0 15 13"><rect x="0.5" y="3" width="9" height="9" fill="none" stroke="#fff" stroke-width="1.3"/><path d="M2.5,7 L5,10 L14,1" fill="none" stroke="#fff" stroke-width="2"/></svg>High Risk Planning</li>
  </ul>

  <div class="abs contact" style="left:48px">
    <svg width="20" height="20" viewBox="0 0 20 20"><circle cx="10" cy="10" r="9" fill="none" stroke="#fff" stroke-width="1.5"/><path d="M6.5,5 L8.5,5 L9.3,7.5 L8,8.5 Q9,11 11.5,12 L12.5,10.7 L15,11.5 L15,13.5 Q10,14.5 6.5,9.5 Q5.7,7 6.5,5 Z" fill="#fff"/></svg>
    555-271-6043
  </div>
  <div class="abs contact" style="left:335px">
    <svg width="22" height="18" viewBox="0 0 22 18"><path d="M1,7 L11,1 L21,7 L21,17 L1,17 Z" fill="#fff"/><path d="M1,7 L11,13 L21,7" fill="none" stroke="#555" stroke-width="1.4"/></svg>
    info@varnelguard.example
  </div>
  <div class="abs contact" style="left:704px">
    <svg width="24" height="24" viewBox="0 0 24 24" fill="none" stroke="#fff" stroke-width="1.5"><circle cx="12" cy="12" r="10"/><ellipse cx="12" cy="12" rx="4.5" ry="10"/><path d="M2,12 H22 M4,6.5 H20 M4,17.5 H20"/></svg>
    www.varnelguard.example
  </div>
</div>
</body>
</html>
```